KTR-OB R-Value Adjustment Paper

This is a technical paper needing professional layout that is compatible with our current style guidelines; it will be used in digital and print media. It has numerous tables and graphs.

We have attached a report "KTR Cladding EPD" issued to our company under Marrowfield Assurance graphic design guidelines. While this does NOT reflect our style branding, it does represent the 'technical' presentation we are looking for.

To view our typical company design/style please see our website at www.ktrcouncil.org. Our primary RGB colors are: (187,140,9); (94,47,29); (94,138,164); and (164,167,15). Secondary RGB colors are (249,162,28) and (218,210,208). Our title/header font is DIN Next LT Pro and our copy font is Calibri 10.5 pt. We can deviate from the font specification if beneficial.

The attached file, "KTR-OB Rvalue Adj Factor" is a partial representation of the full document that will need design services. For the concepts we would like to see a cover/title page, a text/copy page and a sample of data graphic treatments.Once we have agreed upon a design concept we will determine full costs to complete the project.

Target Market(s)

Building and construction professionals, architects, building code officials

Font styles to use
Other font styles liked:
• DIN Next LT Pro

Requirements
Must have
• Design elements that help make the information easy to read and use.
Nice to have
• Right amount of white space.

```html
<!DOCTYPE html>
<html lang="en">
<head>
<meta charset="utf-8">
<title>KTR-OB Rvalue Adj Factor — Moisture</title>
<link rel="stylesheet" href="https://fonts.googleapis.com/css2?family=Barlow:wght@400;500&family=Barlow+Condensed:ital,wght@1,500&display=swap">
<style>
  :root {
    --ink: #111111;
    --heading-grey: #7b7b7b;
    --rule-dark: #6f7308;
    --rule-mid: #a8ad12;
    --rule-light: #c6cc6e;
    --grid: #7a7a7a;
    --eps: #b8900f;
    --xps: #f6a623;
    --paper: #ffffff;
  }
  * { margin: 0; padding: 0; box-sizing: border-box; }
  html, body { width: 848px; height: 1200px; overflow: hidden; background: var(--paper); }
  .page { position: relative; width: 848px; height: 1200px; font-family: "Barlow", Arial, sans-serif; color: var(--ink); }
  .section-title {
    position: absolute; left: 33px;
    font-size: 21px; font-weight: 500; letter-spacing: 1.6px;
    color: var(--heading-grey); text-transform: uppercase;
  }
  .section-rule { position: absolute; left: 32px; width: 784px; height: 8px; }
  .rule-dark { background: var(--rule-dark); }
  .rule-mid { background: var(--rule-mid); }
  .rule-light { background: var(--rule-light); }
  .copy {
    position: absolute; left: 33px; width: 782px;
    font-size: 13.6px; font-weight: 500; letter-spacing: 0.75px; line-height: 22.8px;
  }
  .copy .line { text-align: justify; text-align-last: justify; white-space: nowrap; }
  .copy .line.last { text-align-last: left; }
  .chart { position: absolute; left: 0; top: 360px; }
  .chart text { font-family: "Barlow", Arial, sans-serif; font-size: 13.5px; font-weight: 500; fill: var(--ink); }
  .figure-caption {
    position: absolute; left: 42px; top: 750px;
    font-family: "Barlow Condensed", "Arial Narrow", sans-serif;
    font-style: italic; font-weight: 500; font-size: 18.5px; letter-spacing: 0.2px;
  }
</style>
</head>
<body>
<main class="page">

  <h2 class="section-title" style="top:52px;">Moisture</h2>
  <div class="section-rule rule-dark" style="top:88px;"></div>

  <div class="copy" style="top:127px;">
    <div class="line">The R-value of insulation typically is determined under ideal, dry laboratory conditions.&nbsp; In many building</div>
    <div class="line">applications, polystyrene foam insulation is protected from moisture, and the R-values determined under</div>
    <div class="line">dry laboratory conditions are appropriate.&nbsp; Examples include insulation under roof membranes and wall</div>
    <div class="line">insulation covered by a weather-resistive barrier.&nbsp; In these applications, no adjustment to the R-value is</div>
    <div class="line">needed based on the insulation’s exposure to moisture. Polystyrene foam in ground contact applications</div>
    <div class="line">may be exposed to moisture, and, in such cases, an adjustment to the laboratory R-value based on these</div>
    <div class="line">conditions is appropriate. Under these conditions, the reductions in the R-values of both EPS and XPS</div>
    <div class="line">materials are well documented in international standard ISO/FDIS 10456 (ISO, 2007) and Figure 4 shows</div>
    <div class="line last">the loss of R-value for EPS and XPS as a function of moisture.</div>
  </div>

  <svg class="chart" width="848" height="390" viewBox="0 0 848 390" role="img" aria-label="Line chart of R-value loss versus moisture content for EPS and XPS">
    <g stroke="var(--grid)" stroke-width="2.4" fill="none">
      <line x1="163" y1="18" x2="163" y2="325"/>
      <line x1="231.1" y1="18" x2="231.1" y2="325"/>
      <line x1="299.3" y1="18" x2="299.3" y2="325"/>
      <line x1="367.4" y1="18" x2="367.4" y2="325"/>
      <line x1="435.6" y1="18" x2="435.6" y2="325"/>
      <line x1="503.7" y1="18" x2="503.7" y2="325"/>
      <line x1="571.9" y1="18" x2="571.9" y2="325"/>
      <line x1="640" y1="18" x2="640" y2="325"/>
      <line x1="163" y1="18" x2="640" y2="18"/>
      <line x1="163" y1="79.4" x2="640" y2="79.4"/>
      <line x1="163" y1="140.8" x2="640" y2="140.8"/>
      <line x1="163" y1="202.2" x2="640" y2="202.2"/>
      <line x1="163" y1="263.6" x2="640" y2="263.6"/>
      <line x1="163" y1="325" x2="640" y2="325"/>
    </g>
    <g text-anchor="end">
      <text x="148" y="23">25</text>
      <text x="148" y="84">20</text>
      <text x="148" y="145">15</text>
      <text x="148" y="207">10</text>
      <text x="148" y="268">5</text>
      <text x="148" y="330">0</text>
    </g>
    <g text-anchor="middle">
      <text x="163" y="349">0</text>
      <text x="231.1" y="349">1</text>
      <text x="299.3" y="349">2</text>
      <text x="367.4" y="349">3</text>
      <text x="435.6" y="349">4</text>
      <text x="503.7" y="349">5</text>
      <text x="571.9" y="349">6</text>
      <text x="640" y="349">7</text>
      <text x="405" y="378">Moisture, Value %</text>
      <text transform="translate(121 172) rotate(-90)">R-value Loss, %</text>
    </g>
    <polyline fill="none" stroke="var(--eps)" stroke-width="4" points="163,325 231.1,278.3 299.3,231.7 367.4,187.5 435.6,143.3 503.7,101.5 571.9,63.4"/>
    <polyline fill="none" stroke="var(--xps)" stroke-width="4" points="163,325 231.1,295.5 299.3,264.8 367.4,237.8 435.6,207.1 503.7,180.1 571.9,155.5"/>
    <g fill="var(--eps)">
      <circle cx="163" cy="325" r="5.5"/><circle cx="231.1" cy="278.3" r="5.5"/><circle cx="299.3" cy="231.7" r="5.5"/>
      <circle cx="367.4" cy="187.5" r="5.5"/><circle cx="435.6" cy="143.3" r="5.5"/><circle cx="503.7" cy="101.5" r="5.5"/>
      <circle cx="571.9" cy="63.4" r="5.5"/>
    </g>
    <g fill="var(--xps)">
      <circle cx="231.1" cy="295.5" r="5.5"/><circle cx="299.3" cy="264.8" r="5.5"/>
      <circle cx="367.4" cy="237.8" r="5.5"/><circle cx="435.6" cy="207.1" r="5.5"/><circle cx="503.7" cy="180.1" r="5.5"/>
      <circle cx="571.9" cy="155.5" r="5.5"/>
    </g>
    <line x1="676" y1="187.5" x2="712" y2="187.5" stroke="var(--eps)" stroke-width="4"/>
    <circle cx="694" cy="187.5" r="5.5" fill="var(--eps)"/>
    <text x="717" y="192.5">EPS</text>
    <line x1="676" y1="218" x2="712" y2="218" stroke="var(--xps)" stroke-width="4"/>
    <circle cx="694" cy="218" r="5.5" fill="var(--xps)"/>
    <text x="717" y="223">XPS</text>
  </svg>

  <p class="figure-caption">Figure 4.&nbsp; Loss of R-value by Polystyrene Foam Insulation Due to the Absorption of moisture (ISO, 2007)</p>

  <h2 class="section-title" style="top:804px; left:35px;">Effective R-Value</h2>
  <div class="section-rule rule-mid" style="top:840px; left:33px;"></div>

  <div class="copy" style="top:861px; left:35px;">
    <div class="line">The discussion on temperature, moisture, and aging demonstrated that R-value is affected by each of</div>
    <div class="line">these considerations.&nbsp; A methodology that includes all three considerations can be used to determine the</div>
    <div class="line last">effective R-value under specific building conditions.</div>
  </div>

  <h2 class="section-title" style="top:960px; left:35px;">Effective R-Value Determination</h2>
  <div class="section-rule rule-light" style="top:996px; left:35px; width:783px;"></div>

  <div class="copy" style="top:1029px; left:36px;">
    <div class="line">The adjustment of the R-value from ideal laboratory conditions to the conditions in building applications</div>
    <div class="line">is straightforward.&nbsp; The Effective R-value determination discussed herein is analogous to a thermal</div>
    <div class="line last">conductivity adjustment method recognized in international standard ISO 10456 (ISO, 2007).</div>
  </div>

</main>
</body>
</html>
```